Quarrytide
Quarrytide - Financial Services
Financial Services
www.quarrytidepay.com
Our team has been providing solutions for workers compensation for business owners for over 22 years, our service is provoided at no charge (as it is paid for by the vendor). What makes us unique is our ability to write just about every size company (3 man to 1000) and industry in every state,. Our programs simlyfy the business owners way of doing business by eliminationg several annoying functions that business owners face. For example, with our program a business owner would write one check for payroll, that check would cover his payroll, workers compensation, payroll taxes, employee deductions and garnishments, direct deposit and benefit deductions, year end W-2's and the liabilities that come with year end W-2's. Our program we keeps business owners compliant by keeping them informed about new requirements, labor laws, we provide all employee applications, safety posters, they are able to call with any employee related questions about hiring and firing and so on. All usually for less that they can do it themselves.
Busy, wordy
Service Oriented
White/possible grey, logo colors
Blues and whites and greys, logo colors
left side
We have a content writer completing the text, our home page will contain very little text and focus more as a landing page. The site itself needs to be very clean, simple and easy to navigate but will also allow viewers to go deep into the site if they want to find information, yet at the same time it will not force people away because of too much content

```html
<!DOCTYPE html>
<html lang="en">
<head>
<meta charset="utf-8">
<title>Quarrytide – Financial Services</title>
<link href="https://fonts.googleapis.com/css2?family=Open+Sans:wght@400;600;700&display=swap" rel="stylesheet">
<style>
:root{
  --blue:#1e9ad6;
  --blue-dark:#0a6fae;
  --blue-light:#6cc6ee;
  --ink:#3a3a3a;
  --muted:#8c8c8c;
  --grey-top:#f4f4f4;
  --grey-mid:#d6d6d6;
  --white:#ffffff;
}
*{margin:0;padding:0;box-sizing:border-box}
html,body{width:1200px;height:1000px;overflow:hidden}
body{font-family:"Open Sans",Arial,sans-serif;color:var(--ink);background:var(--white);position:relative}

.site-header{position:absolute;left:0;top:0;width:1200px;height:165px;
  background:linear-gradient(180deg,var(--grey-top) 0%,#e6e6e6 70%,var(--grey-mid) 100%)}
.brand{position:absolute;left:115px;top:58px;display:flex;align-items:center;gap:14px}
.brand-mark{width:72px;height:72px;border-radius:50%;background:var(--blue)}
.brand-name{font-size:44px;font-weight:700;color:#2b5c86;letter-spacing:1px;text-transform:uppercase}
.contact{position:absolute;right:140px;top:80px;text-align:left}
.contact-label{font-size:22px;color:#777}
.contact-phone{font-size:26px;color:var(--blue);font-weight:600;letter-spacing:1px}

.main-nav{position:absolute;left:0;top:165px;width:1200px;height:40px;
  background:linear-gradient(180deg,#5a5a5a,#3d3d3d)}
.main-nav a{position:absolute;top:0;height:40px;line-height:40px;font-size:14px;color:#e8e8e8;text-decoration:none}
.main-nav a.active{background:linear-gradient(180deg,#d9d9d9,#a9a9a9);color:#555;padding:0 26px;left:108px}

.hero{position:absolute;left:0;top:205px;width:1200px;height:385px;
  background:linear-gradient(180deg,var(--blue-light) 0%,var(--blue) 40%,var(--blue-dark) 100%)}
.slider{position:absolute;left:108px;top:30px;width:975px;height:335px;background:var(--white);overflow:hidden}
.slider svg{position:absolute;left:0;top:0}
.slide-copy{position:absolute;left:597px;top:118px}
.slide-title{font-size:30px;font-weight:400;color:#555;line-height:1.2;text-transform:uppercase;white-space:nowrap}
.slide-sub{font-size:15px;color:var(--blue);margin-top:6px;text-transform:uppercase;white-space:nowrap}
.dots{position:absolute;right:20px;bottom:12px;display:flex;gap:6px}
.dots span{width:14px;height:14px;border-radius:50%;background:#c9c9c9}
.dots span.on{background:var(--blue)}

.features{position:absolute;left:118px;top:630px;width:990px;display:flex;gap:30px}
.feature{width:225px}
.feature h2{font-size:17px;font-weight:600;line-height:1.2;text-transform:uppercase;color:#333;height:42px;white-space:nowrap}
.feature .tag{margin-top:10px;width:205px;height:18px;background:linear-gradient(180deg,#3aaee4,var(--blue-dark));
  color:var(--white);font-size:9px;line-height:18px;padding-left:10px;white-space:nowrap;overflow:hidden}
.feature p{margin-top:14px;width:205px;font-size:11px;line-height:1.85;color:var(--muted)}
.feature .more{display:block;margin-top:20px;font-size:11px;font-weight:700;color:var(--blue-dark);text-decoration:none;text-transform:uppercase}

.site-footer{position:absolute;left:0;top:890px;width:1200px;height:110px;
  background:linear-gradient(180deg,#8a8a8a 0%,#c9c9c9 60%,#e3e3e3 100%)}
.copyright{position:absolute;left:135px;top:22px;font-size:14px;color:var(--white)}
.follow{position:absolute;left:875px;top:22px;display:flex;align-items:center;gap:10px;font-size:14px;color:#eee}
.follow span.icon{width:22px;height:22px;background:#3c3c3c;border-radius:3px}
</style>
</head>
<body>

<header class="site-header">
  <div class="brand">
    <div class="brand-mark"></div>
    <div class="brand-name">Quarrytide</div>
  </div>
  <div class="contact">
    <div class="contact-label">Contact Us Now</div>
    <div class="contact-phone">888.555.0147</div>
  </div>
</header>

<nav class="main-nav">
  <a class="active" href="#">Home</a>
  <a href="#" style="left:245px">About Us</a>
  <a href="#" style="left:372px">Services</a>
  <a href="#" style="left:490px">Portfolio</a>
  <a href="#" style="left:612px">Contact</a>
</nav>

<section class="hero">
  <div class="slider">
    <svg width="975" height="335" viewBox="0 0 975 335" role="img" aria-label="Photo of a large steel globe sculpture in front of city office towers">
      <defs>
        <linearGradient id="photoTone" x1="0" y1="0" x2="0" y2="1">
          <stop offset="0" stop-color="#aeb9c6"/>
          <stop offset="0.55" stop-color="#6f7a86"/>
          <stop offset="1" stop-color="#2f3438"/>
        </linearGradient>
      </defs>
      <path d="M0 0 H540 C600 70 600 260 560 335 H0 Z" fill="url(#photoTone)"/>
      <path d="M540 0 C600 70 600 260 560 335" fill="none" stroke="#1e9ad6" stroke-width="5"/>
    </svg>
    <div class="slide-copy">
      <h1 class="slide-title">We are experts in the<br>financial industry</h1>
      <div class="slide-sub">See what we can do for you</div>
    </div>
    <div class="dots"><span></span><span class="on"></span><span></span></div>
  </div>
</section>

<main class="features">
  <article class="feature">
    <h2>Excellent solution<br>for your business</h2>
    <div class="tag">Start of new client program</div>
    <p>Our team handles payroll, compensation and taxes in one simple step, so owners can focus on running their company every day of the year with less paperwork and fewer calls.</p>
    <a class="more" href="#">Read more »</a>
  </article>
  <article class="feature">
    <h2>Time saving program<br>for companies</h2>
    <div class="tag">One check covers it all</div>
    <p>Write a single check that covers wages, deductions, garnishments and deposits, and let our staff take care of the filings and year end forms that come with every payroll.</p>
    <a class="more" href="#">Read more »</a>
  </article>
  <article class="feature">
    <h2>Testimonials from<br>our valued clients</h2>
    <div class="tag">Kmortiglan, Copperline Wealth</div>
    <p>Switching to this program saved our office hours each week and kept us compliant with new labor laws, all for less than we used to spend doing it ourselves in house.</p>
    <a class="more" href="#">Read more »</a>
  </article>
  <article class="feature">
    <h2>Latest news &amp;<br>events</h2>
    <div class="tag">August 04, 2011</div>
    <p>New safety posters and updated employee applications are now ready for every state, and our advisors are available to answer questions about hiring and more.</p>
    <a class="more" href="#">Read more »</a>
  </article>
</main>

<footer class="site-footer">
  <div class="copyright">© Copyright 2011 Quarrytide Works. All Rights Reserved</div>
  <div class="follow">Follow us <span class="icon"></span><span class="icon"></span><span class="icon"></span><span class="icon"></span></div>
</footer>

</body>
</html>
```